Poster for List of Company Values

We need a poster to outline our Values which will be displayed in our office as well as posted on our website and other platforms (so need to allow for some flexibly in its application).

File attached outlines what we currently have with design and also our company style guide.

Note that we are looking for a modern, clean look, which still represents our core activities of construction and environmental services.

You can also reference our website here:

https://quorvelgroup.com.au/

Happy to answer any questions you might have.

Thanks for your interest,
Brent

Target Market(s)

Internal and External clients

Industry/Entity Type

Construction, water and recycling

Font styles to use
Sans Serif

Requirements
Must have
• All values on the one page. Graphic to represent each value. Also needs to use company logo
Nice to have
• Preference for poster to be orientated in landscape
Should not have
• Do not follow example provided, this is only to demonstrate what we have to date and also the text required

```html
<!DOCTYPE html>
<html lang="en">
<head>
<meta charset="utf-8">
<title>Our Core Values – Quorvel Group</title>
<link rel="stylesheet" href="https://fonts.googleapis.com/css2?family=Open+Sans:ital,wght@0,400;0,700;1,700&family=Source+Sans+3:wght@400;700&display=swap">
<style>
  :root{
    --bg:#f8f8f8;
    --navy:#0d3d8a;
    --ink:#3a383a;
    --body:#333333;
    --rule:#d4d4d8;
    --loyal:#575355;
    --initiative:#45b149;
    --team:#d2274a;
    --respect-seg:#ddbe5a;
    --respect:#6564b0;
    --honest:#f28a45;
    --positive:#08bbaa;
  }
  *{margin:0;padding:0;box-sizing:border-box}
  html,body{width:1200px;height:848px;overflow:hidden;background:var(--bg)}
  .poster{position:relative;width:1200px;height:848px;background:var(--bg);font-family:"Open Sans",sans-serif;color:var(--body)}
  .wheel{position:absolute;left:0;top:0}
  .wheel__title{font-family:"Source Sans 3",sans-serif;fill:#fff;text-anchor:middle}
  .wheel__num{font-family:"Source Sans 3",sans-serif;font-size:64px;fill:none;stroke:#fff;stroke-width:1.4;text-anchor:middle}

  .divider{position:absolute;width:1px;background:var(--rule)}

  .icon{position:absolute;width:74px;height:74px;border-radius:50%;opacity:.22}

  .value{position:absolute;width:170px;text-align:center}
  .value__lead{font-family:"Source Sans 3",sans-serif;font-size:25px;line-height:24px;font-weight:400}
  .value__word{font-family:"Source Sans 3",sans-serif;font-size:44px;line-height:40px;font-weight:700;letter-spacing:-1.5px}
  .value__sub{font-size:15px;font-weight:700;color:var(--ink);line-height:19px;margin-bottom:1px}
  .value__text{font-size:14.5px;line-height:19.4px;margin-top:13px}

  .value--loyal{left:42px;top:283px}
  .value--loyal .value__lead,.value--loyal .value__word{color:var(--ink)}
  .value--initiative{left:232px;top:403px}
  .value--initiative .value__lead,.value--initiative .value__word{color:var(--initiative)}
  .value--team{left:422px;top:461px}
  .value--team .value__lead,.value--team .value__word{color:var(--team)}
  .value--respect{left:611px;top:461px}
  .value--respect .value__lead,.value--respect .value__word{color:var(--respect)}
  .value--honest{left:801px;top:403px}
  .value--honest .value__lead,.value--honest .value__word{color:var(--honest)}
  .value--positive{left:991px;top:283px}
  .value--positive .value__lead,.value--positive .value__word{color:var(--positive)}
  .value--positive .value__sub{margin-top:20px}
  .value--positive .value__text{margin-top:0}

  .site{position:absolute;left:43px;top:760px}
  .site__bar{width:109px;height:5px;background:var(--navy)}
  .site__url{margin-top:12px;font-style:italic;font-weight:700;font-size:20px;color:var(--ink);letter-spacing:.2px}

  .brand{position:absolute;left:934px;top:740px;display:flex;align-items:center;gap:12px}
  .brand__mark{width:52px;height:52px;background:var(--navy)}
  .brand__name{font-family:"Open Sans",sans-serif;font-weight:700;font-size:27px;line-height:27px;color:var(--ink)}
</style>
</head>
<body>
<main class="poster">
  <svg class="wheel" width="1200" height="848" viewBox="0 0 1200 848" aria-hidden="true">
    <line x1="26" y1="187" x2="277" y2="105" stroke="#dcdcf0" stroke-dasharray="5 4"/>
    <line x1="923" y1="105" x2="1176" y2="187" stroke="#dcdcf0" stroke-dasharray="5 4"/>
    <line x1="345" y1="230" x2="273" y2="293" stroke="#ececec"/>
    <line x1="459" y1="315" x2="421" y2="403" stroke="#ececec"/>
    <line x1="741" y1="315" x2="796" y2="442" stroke="#ececec"/>
    <line x1="855" y1="230" x2="985" y2="350" stroke="#ececec"/>
    <line x1="600" y1="345" x2="600" y2="440" stroke="#ececec"/>
    <path d="M266 0 A334 334 0 0 0 934 0 Z" fill="var(--navy)"/>
    <path d="M600 0 L282.3 103.2 A334 334 0 0 0 351.8 223.5 Z" fill="var(--loyal)"/>
    <path d="M600 0 L351.8 223.5 A334 334 0 0 0 464.2 305.1 Z" fill="var(--initiative)"/>
    <path d="M600 0 L464.2 305.1 A334 334 0 0 0 600 334 Z" fill="var(--team)"/>
    <path d="M600 0 L600 334 A334 334 0 0 0 735.8 305.1 Z" fill="var(--respect-seg)"/>
    <path d="M600 0 L735.8 305.1 A334 334 0 0 0 848.2 223.5 Z" fill="var(--honest)"/>
    <path d="M600 0 L848.2 223.5 A334 334 0 0 0 917.7 103.2 Z" fill="var(--positive)"/>
    <circle cx="600" cy="0" r="209" fill="var(--navy)" stroke="#fff" stroke-width="4"/>
    <text class="wheel__title" x="600" y="69" font-size="43">OUR CORE</text>
    <text class="wheel__title" x="600" y="134" font-size="70" font-weight="700">VALUES</text>
    <text class="wheel__num" x="361" y="162">01</text>
    <text class="wheel__num" x="437" y="246">02</text>
    <text class="wheel__num" x="545" y="296">03</text>
    <text class="wheel__num" x="657" y="296">04</text>
    <text class="wheel__num" x="763" y="246">05</text>
    <text class="wheel__num" x="839" y="162">06</text>
  </svg>

  <div class="divider" style="left:222px;top:353px;height:221px"></div>
  <div class="divider" style="left:412px;top:438px;height:224px"></div>
  <div class="divider" style="left:601px;top:456px;height:232px"></div>
  <div class="divider" style="left:791px;top:438px;height:224px"></div>
  <div class="divider" style="left:981px;top:350px;height:225px"></div>

  <div class="icon" role="img" aria-label="Icon: star above an open hand" style="left:219px;top:151px;background:var(--loyal)"></div>
  <div class="icon" role="img" aria-label="Icon: gear with a light bulb" style="left:306px;top:280px;background:var(--initiative)"></div>
  <div class="icon" role="img" aria-label="Icon: three hands joined in a circle" style="left:470px;top:350px;background:var(--team)"></div>
  <div class="icon" role="img" aria-label="Icon: two hands clasped" style="left:659px;top:350px;background:var(--respect)"></div>
  <div class="icon" role="img" aria-label="Icon: hand held over a heart" style="left:828px;top:272px;background:var(--honest)"></div>
  <div class="icon" role="img" aria-label="Icon: light bulb with a plus sign" style="left:915px;top:159px;background:var(--positive)"></div>

  <section class="value value--loyal">
    <p class="value__lead">BE</p>
    <p class="value__word">loyal</p>
    <p class="value__text">We take care of our own and&nbsp; provide opportunities to listen and support each other.</p>
  </section>
  <section class="value value--initiative">
    <p class="value__lead">SHOW</p>
    <p class="value__word">initiative</p>
    <p class="value__text">We celebrate and recognize our own and encourage forward thinking.</p>
  </section>
  <section class="value value--team">
    <p class="value__lead">THINK</p>
    <p class="value__word">team</p>
    <p class="value__text">We communicate effectively and work as a team by helping and supporting each other.</p>
  </section>
  <section class="value value--respect">
    <p class="value__lead">SHOW</p>
    <p class="value__word">respect</p>
    <p class="value__text">We value the diversity and opinions of all.</p>
  </section>
  <section class="value value--honest">
    <p class="value__lead">BE OPEN &amp;</p>
    <p class="value__word">honest</p>
    <p class="value__text">We are clear and open with each other, and provide an approach-able and friendly envi-ronment.</p>
  </section>
  <section class="value value--positive">
    <p class="value__lead">BE</p>
    <p class="value__word">positive</p>
    <p class="value__sub">SMILE</p>
    <p class="value__text">We are solutions focused and encourage a positive attitude turning a negative into a positive.</p>
  </section>

  <footer class="site">
    <div class="site__bar"></div>
    <p class="site__url">www.quorvelgroup.com.au</p>
  </footer>

  <div class="brand">
    <span class="brand__mark"></span>
    <p class="brand__name">QUORVEL<br>Group</p>
  </div>
</main>
</body>
</html>
```